Start-Up Property Development Company Requires Word Press Website Design

A new property development company in Sydney requires a new website.
This version (Version 1) is very simple and will represent one, small aspect of what the company does, which is acquiring properties for redevelopment:

Needed:
- 1 page incorporating copy, logo and illustration.
- Email contact form.
- Contact information.

It will be expanded in the next few months to include another section for marketing homes for sale (Version 2). This section should sit on top of the Version 1 (in the top section of the same scrolling page).

So this initial design must be able to simply incorporate the expansion.

The site design needs to:
- Take up the entire width of the monitor.
- Not be too different from companies corporate look and feel.
- Be simple, functional and elegant.
- Have a long scroll (1 page) with navigation items at the top of the screen simply linking to the corresponding section lower in the page.

Reason: Not happy with the choice of designs. I'm wanting something clean and fresh and not too intensive with graphics.

```html
<!DOCTYPE html>
<html lang="en">
<head>
<meta charset="utf-8">
<title>Korvale Property</title>
<link href="https://fonts.googleapis.com/css2?family=Lato:wght@300;400;700;900&family=Tinos&display=swap" rel="stylesheet">
<style>
:root{
  --red:#c8161d;
  --ink:#111111;
  --white:#ffffff;
  --footer-grey:#7f868b;
  --field-border:#c9c9c9;
  --nav-top:#5a5a5a;
  --nav-bottom:#050505;
  --hero-sky:#c9cdc4;
  --hero-field:#6f8f4a;
  --hero-overlay:rgba(40,44,42,.55);
}
*{box-sizing:border-box;margin:0;padding:0}
html,body{width:847px;height:1200px;overflow:hidden;background:var(--white)}
body{position:relative;font-family:'Lato',sans-serif;color:var(--ink)}

.site-header{position:absolute;left:0;top:0;width:847px;height:86px}
.brand{position:absolute;left:26px;top:26px;display:flex;align-items:center;gap:6px;
  font-weight:900;font-size:19px;letter-spacing:-.2px;color:var(--ink);line-height:1}
.brand-mark{width:12px;height:12px;background:var(--red)}
.header-contact{position:absolute;right:22px;top:14px;text-align:right;font-size:12px;line-height:14px}
.header-contact .email{margin-top:13px}

.main-nav{position:absolute;left:26px;top:87px;width:802px;height:41px;
  background:linear-gradient(var(--nav-top),var(--nav-bottom));display:flex}
.main-nav a{font-family:'Tinos',serif;font-size:14px;color:#a9a9a9;text-decoration:none;
  line-height:41px;padding:0 19px}
.main-nav a.active{background:var(--red);color:var(--white);padding:0 21px}

.hero{position:absolute;left:26px;top:129px;width:802px;height:385px;
  background:linear-gradient(180deg,var(--hero-sky) 0%,#9ea59b 55%,var(--hero-field) 100%)}
.hero-panel{position:absolute;left:401px;top:0;width:401px;height:385px;background:var(--hero-overlay)}
.hero-copy{position:absolute;left:426px;top:146px;width:345px;color:var(--white);
  font-weight:300;font-size:10.5px;line-height:12.5px}
.hero-copy p{margin-bottom:11px}
.hero-copy .name{font-weight:700;font-size:16px}
.hero-copy em{font-family:'Tinos',serif;font-weight:700}

.email-section h2{position:absolute;left:26px;top:553px;font-size:28px;font-weight:700}
.contact-form{position:absolute;left:284px;top:639px;width:296px}
.field{display:block;width:296px;border:1px solid var(--field-border);
  font-family:'Tinos',serif;font-size:14px;color:#555;padding:0 10px;margin-bottom:2px}
.field.short{height:43px;line-height:41px}
.field.message{height:82px;padding-top:12px}
.submit{width:296px;height:43px;margin-top:1px;border-radius:2px;
  background:linear-gradient(#5c5c5c,#1c1c1c);color:var(--white);
  font-family:'Tinos',serif;font-size:18px;text-align:center;line-height:43px}

.site-footer{position:absolute;left:0;top:857px;width:847px;height:300px;background:var(--footer-grey);color:var(--white)}
.site-footer h2{position:absolute;left:22px;top:34px;font-size:28px;font-weight:700}
.footer-details{position:absolute;left:424px;top:94px;font-size:14px;line-height:17px;font-weight:300}
.footer-details strong{font-weight:700}
.footer-details .block{margin-bottom:17px}
.footer-details .email{margin-top:35px}
.copyright{position:absolute;left:0;top:1157px;width:847px;height:43px;background:#000;
  color:var(--white);font-size:9px;font-weight:700;text-align:center;line-height:40px;font-family:Arial,sans-serif}
</style>
</head>
<body>
<header class="site-header">
  <div class="brand"><span class="brand-mark"></span>KORVALE PROPERTY</div>
  <div class="header-contact">
    <div><strong>Tel:</strong> 02 9000 4821</div>
    <div><strong>Mob:</strong> 0400 127 356</div>
    <div class="email">sam@korvale.com.au</div>
  </div>
</header>

<nav class="main-nav">
  <a class="active" href="#home">HOME</a>
  <a href="#contact">CONTACT INFO</a>
  <a href="#email">EMAIL US</a>
</nav>

<section class="hero" id="home" role="img" aria-label="Photo of two hands framing a glass pane showing a building wireframe over a green field">
  <div class="hero-panel"></div>
  <div class="hero-copy">
    <p><span class="name">Korvale Property</span> is property development company located in Sydney. We are currently searching for properties to acquire and redevelop.</p>
    <p>We value properties using their potential value following redevelpment, rather than the commonly used methods of recent, comparative sales and the opinions of agents. Because of this we can sometimes offer more than what is typical for your local market.</p>
    <p><span class="name" style="font-size:14px">Korvale Property</span> is <em>not</em> a real estate agency, so <em>you won't have to pay</em> a real estate agents commission for the sale of your property should you decide to work with us.</p>
    <p>So if you're thinking of selling or interested in knowing what we think your property is worth, please <strong>contact us!</strong></p>
  </div>
</section>

<section class="email-section" id="email">
  <h2>Email Us</h2>
  <form class="contact-form">
    <div class="field short">Name</div>
    <div class="field short">Your Email Id</div>
    <div class="field message">Messsage</div>
    <div class="submit">SUBMIT</div>
  </form>
</section>

<footer class="site-footer" id="contact">
  <h2>Contact Us</h2>
  <div class="footer-details">
    <div class="block"><strong>Korvale Pty Ltd</strong><br>P.O. Box 12<br>Surry Hills NSW 2010</div>
    <div><strong>Tel:</strong> 02 9000 4821<br><strong>Mob:</strong> 0400 127 356</div>
    <div class="email">sam@<strong>korvale</strong>.com.au</div>
  </div>
</footer>
<div class="copyright">Copyright : Korvale Pty Ltd</div>
</body>
</html>
```